Painting Contractor Business Card Design

We are looking for a cool, bold, modern, polished, business card design. We are a high-end residential painting contractor. Please incorporate our logo and keep with our green/black color scheme. We are interested in seeing 2-sided and 1-sided options. Thank you very much!

Industry/Entity Type

Business

Contact Information for Business Card

Info for the card:
Owen Talsky
mobile 206-555-0193
email owen@kestrowfinish.net
web www.kestrowfinish.net

```html
<!DOCTYPE html>
<html lang="en">
<head>
<meta charset="utf-8">
<title>Kestrow Finish – Business Card</title>
<link rel="stylesheet" href="https://fonts.googleapis.com/css2?family=Montserrat:wght@600&family=PT+Sans:wght@400;700&display=swap">
<style>
  :root {
    --backdrop: #ece8e3;
    --card: #ffffff;
    --card-edge: #1c1c1c;
    --ink-navy: #1d5384;
    --ink-green: #22a36a;
    --ink-gold: #e7b21c;
    --ink-orange: #ec5a28;
    --brand-green: #35a84a;
  }
  * { box-sizing: border-box; margin: 0; padding: 0; }
  html, body { width: 1200px; height: 793px; overflow: hidden; }
  body {
    background: var(--backdrop);
    position: relative;
    font-family: "PT Sans", sans-serif;
  }
  .card {
    position: absolute;
    background: var(--card);
    border: 2px solid var(--card-edge);
    border-radius: 26px;
    overflow: hidden;
  }
  .card--front {
    left: 110px; top: 90px;
    width: 420px; height: 612px;
  }
  .card--back {
    left: 570px; top: 220px;
    width: 560px; height: 330px;
  }

  /* front side */
  .front-mark {
    position: absolute;
    left: 0; right: 0; top: 110px;
    display: flex; flex-direction: column; align-items: center; gap: 14px;
  }
  .front-mark__square {
    width: 96px; height: 96px;
    background: var(--brand-green);
  }
  .front-mark__name {
    font-family: "Montserrat", sans-serif;
    font-weight: 600;
    font-size: 30px;
    letter-spacing: 1px;
    color: var(--brand-green);
  }
  .contact {
    position: absolute;
    left: 100px; top: 392px;
    line-height: 1.18;
  }
  .contact__name {
    font-weight: 700; font-size: 28px;
    color: var(--ink-navy);
  }
  .contact__phone { font-size: 23px; color: var(--ink-green); }
  .contact__email { font-size: 23px; color: var(--ink-gold); }
  .contact__web {
    font-size: 23px; color: var(--ink-orange);
    margin-top: 24px;
  }

  /* back side */
  .brush-art {
    position: absolute;
    left: 90px; top: 0;
    width: 400px; height: 240px;
    background: linear-gradient(90deg,
      #c62a2a 0%, #d8c21e 18%, #8fa823 34%, #24a546 50%,
      #2b7fd0 66%, #6a2fb0 82%, #c43ac9 100%);
    opacity: 0.85;
    border-radius: 0 0 18px 18px;
  }
  .back-brand {
    position: absolute;
    left: 62px; top: 248px;
    display: flex; align-items: center; gap: 14px;
  }
  .back-brand__square {
    width: 52px; height: 52px;
    background: var(--brand-green);
  }
  .back-brand__name {
    font-family: "Montserrat", sans-serif;
    font-weight: 600;
    font-size: 38px;
    letter-spacing: 1px;
    color: var(--brand-green);
  }
</style>
</head>
<body>
  <section class="card card--front">
    <div class="front-mark">
      <div class="front-mark__square"></div>
      <div class="front-mark__name">KESTROW FINISH</div>
    </div>
    <div class="contact">
      <p class="contact__name">Owen Talsky</p>
      <p class="contact__phone">206-555-0193</p>
      <p class="contact__email">owen@kestrowfinish.net</p>
      <p class="contact__web">www.kestrowfinish.net</p>
    </div>
  </section>

  <section class="card card--back">
    <div class="brush-art" role="img" aria-label="Row of seven paintbrushes dripping red, yellow, olive, green, blue, purple and magenta paint"></div>
    <div class="back-brand">
      <div class="back-brand__square"></div>
      <div class="back-brand__name">KESTROW FINISH</div>
    </div>
  </section>
</body>
</html>
```